BHAG Poster

We like creativity and visual boxes and shapes not just bullet points. We think we want it to be landscape view. Here are some of the parameters:

BHAG:
Become one of the most admired construction companies in the markets we serve within the next 10 years

3 – 5 year goals:
1. Generate 35m in revenue by 2020
2. Have a 50/50 mix of Public-Private job mix
3. Maintain 15% annual growth

1 year goals:
1. $24M in revenue with better margins
2. 14% gross margin on year
3. Business development begins to pay off
4. Continue recruiting great & talented people

Dynamic Quarter Goal:
(Leave this area blank so we can fill it in each quarter please)

Industry/Entity Type

Landscape

Colors
0355a3

Requirements
Must have
• SHAPES OR BOXES FOR VISUAL EFFECT. We don't want it to just be words on a page. Must be creative. Must have our logo somewhere on the poster. Our cmyk blue color is 100-80-0-22. Poster can have different colors, but it just needs to have some of our blue in it.
Should not have
• no bullet points

```html
<!DOCTYPE html>
<html lang="en">
<head>
<meta charset="utf-8">
<title>BHAG Poster</title>
<link href="https://fonts.googleapis.com/css2?family=Montserrat:wght@500;800&family=Oswald:wght@300;500&family=Roboto:wght@700&display=swap" rel="stylesheet">
<style>
  :root {
    --stage: #3d3d3d;
    --scene: #474747;
    --panel: #bdbdbd;
    --panel-line: #5a5a5a;
    --quarter-label: #cdcdcd;
    --blue-light: #8db6ec;
    --blue-mid: #4f8fe6;
    --blue-deep: #1f69d0;
    --blue-watermark: #3a80e0;
    --divider: #3d3d3d;
    --white: #ffffff;
    --soft-white: rgba(255,255,255,0.88);
    --label: #f2f2f2;
  }
  * { margin: 0; padding: 0; box-sizing: border-box; }
  html, body { width: 1200px; height: 798px; overflow: hidden; background: var(--stage); }
  .poster { position: relative; width: 1200px; height: 798px; background: var(--stage); font-family: "Oswald", sans-serif; }

  .scene-art {
    position: absolute; left: 40px; top: 8px; width: 790px; height: 740px;
    border-radius: 6px;
    background: linear-gradient(180deg, #4a4a4a 0%, var(--scene) 60%, #444 100%);
  }

  .brand { position: absolute; left: 630px; top: 40px; display: flex; align-items: center; gap: 10px; }
  .brand-square { width: 50px; height: 50px; background: var(--white); }
  .brand-name {
    font-family: "Oswald", sans-serif; font-weight: 500; color: var(--white);
    font-size: 25px; line-height: 1.05; letter-spacing: 1px; text-transform: uppercase;
  }

  .goal-bar { position: absolute; display: flex; flex-direction: column; }
  .goal-cell {
    display: flex; flex-direction: column; align-items: center; justify-content: center;
    text-align: center; color: var(--white); border-bottom: 2px solid var(--divider);
  }
  .goal-cell:last-child { border-bottom: none; }
  .goal-figure { font-family: "Montserrat", sans-serif; font-weight: 800; font-size: 29px; line-height: 1; }
  .goal-note { font-weight: 300; font-size: 14.5px; color: var(--soft-white); text-transform: uppercase; line-height: 1.55; margin-top: 6px; letter-spacing: -0.2px; }
  .goal-icon { width: 36px; height: 26px; margin-bottom: 6px; }

  .bar-year { left: 238px; top: 402px; width: 130px; height: 344px; background: var(--blue-light); }
  .bar-year .goal-cell:nth-child(1) { height: 96px; }
  .bar-year .goal-cell:nth-child(2) { height: 76px; }
  .bar-year .goal-cell:nth-child(3) { height: 96px; }
  .bar-year .goal-cell:nth-child(4) { flex: 1; }

  .bar-midterm { left: 390px; top: 317px; width: 131px; height: 429px; background: var(--blue-mid); }
  .bar-midterm .goal-cell:nth-child(1) { height: 140px; }
  .bar-midterm .goal-cell:nth-child(2) { height: 149px; }
  .bar-midterm .goal-cell:nth-child(3) { flex: 1; }

  .bar-bhag { position: absolute; left: 542px; top: 246px; width: 132px; height: 501px; background: var(--blue-deep); overflow: hidden; }
  .bhag-word {
    position: absolute; left: 66px; top: 255px; transform: translate(-50%, -50%) rotate(-90deg);
    font-family: "Montserrat", sans-serif; font-weight: 800; font-size: 92px; letter-spacing: 2px;
    color: var(--blue-watermark); white-space: nowrap;
  }
  .bhag-star { position: absolute; left: 48px; top: 155px; width: 36px; height: 36px; }
  .bhag-statement {
    position: absolute; left: 0; top: 203px; width: 100%; text-align: center;
    font-weight: 300; font-size: 18px; line-height: 26px; color: var(--white); text-transform: uppercase;
  }

  .horizon-label {
    position: absolute; top: 750px; font-family: "Montserrat", sans-serif; font-weight: 500;
    font-size: 23px; color: var(--label); text-align: center; width: 150px;
  }

  .quarter-board { position: absolute; left: 888px; top: 0; width: 312px; height: 798px; background: var(--panel); }
  .quarter { position: absolute; left: 0; width: 100%; display: flex; align-items: center; justify-content: center; border-bottom: 1px solid var(--panel-line); }
  .quarter:last-child { border-bottom: none; }
  .quarter-name { font-family: "Roboto", sans-serif; font-weight: 700; font-size: 50px; color: var(--quarter-label); }
  .q1 { top: 0; height: 175px; }
  .q2 { top: 175px; height: 225px; }
  .q3 { top: 400px; height: 202px; }
  .q4 { top: 602px; height: 196px; }
</style>
</head>
<body>
<main class="poster">
  <div class="scene-art" role="img" aria-label="Illustration of a tower crane lifting the ten-year goal block above a grey city skyline"></div>

  <div class="brand">
    <span class="brand-square"></span>
    <span class="brand-name">Hartwell<br>Construction</span>
  </div>

  <section class="goal-bar bar-year" aria-label="One year goals">
    <div class="goal-cell"><span class="goal-figure">$24M</span><span class="goal-note">Revenue w/ better margin</span></div>
    <div class="goal-cell"><span class="goal-figure">14%</span><span class="goal-note">Gross margin on year</span></div>
    <div class="goal-cell">
      <svg class="goal-icon" viewBox="0 0 36 26" fill="none" stroke="#fff" stroke-width="1.6" stroke-linejoin="round" aria-hidden="true">
        <path d="M2 6 L8 4 L14 8 L22 5 L28 8 L34 6 L34 16 L28 18 L20 23 L16 20 L10 18 L2 16 Z"/>
        <path d="M14 8 L20 14 M17 19 L22 15 M20 22 L25 17"/>
      </svg>
      <span class="goal-note">Business development<br>begins to pay off</span>
    </div>
    <div class="goal-cell">
      <svg class="goal-icon" viewBox="0 0 36 26" fill="none" stroke="#fff" stroke-width="1.6" aria-hidden="true">
        <circle cx="13" cy="8" r="5"/><path d="M3 24 C3 16 23 16 23 24 Z"/>
        <circle cx="23" cy="7" r="4.5"/><path d="M20 15 C28 14 33 17 33 23 L25 23"/>
      </svg>
      <span class="goal-note">Recruit great talent</span>
    </div>
  </section>

  <section class="goal-bar bar-midterm" aria-label="Three to five year goals">
    <div class="goal-cell"><span class="goal-figure">$35M</span><span class="goal-note">In revenue by 2020</span></div>
    <div class="goal-cell"><span class="goal-figure">15%</span><span class="goal-note">Annual growth rate</span></div>
    <div class="goal-cell"><span class="goal-figure">50/50</span><span class="goal-note">Public / private job mix</span></div>
  </section>

  <section class="bar-bhag" aria-label="Ten year goal">
    <span class="bhag-word" aria-hidden="true">BHAG</span>
    <svg class="bhag-star" viewBox="0 0 36 36" fill="none" stroke="#fff" stroke-width="1.6" stroke-linejoin="round" aria-hidden="true">
      <path d="M18 2 L22.3 13.3 L34 13.6 L24.8 21 L28 33 L18 26 L8 33 L11.2 21 L2 13.6 L13.7 13.3 Z"/>
    </svg>
    <p class="bhag-statement">Become one of<br>the most admired<br>construction<br>companies in the<br>markets we serve</p>
  </section>

  <span class="horizon-label" style="left:228px">1 YEAR</span>
  <span class="horizon-label" style="left:380px">3–5 YEARS</span>
  <span class="horizon-label" style="left:532px">10 YEARS</span>

  <aside class="quarter-board" aria-label="Quarterly goals">
    <div class="quarter q1"><span class="quarter-name">Q1</span></div>
    <div class="quarter q2"><span class="quarter-name">Q2</span></div>
    <div class="quarter q3"><span class="quarter-name">Q3</span></div>
    <div class="quarter q4"><span class="quarter-name">Q4</span></div>
  </aside>
</main>
</body>
</html>
```